Corvale Spine & Joint Business Card

Need a business card using the logo provided. I want brand side of the card to be grey with the logo in the center of the card in white.

On the other side I leave to the designers

Target Market(s)

Personal Injury Attorneys

Industry/Entity Type

Medical

Contact Information for Business Card

Name, CEO. Cell Phone, (Brookmere, Address, Phone) (Westhaven, Address, Phone) (Larkfield, Address, Phone)

Colors

Designer to choose only greyscale colors for use in the design.

Requirements
Must have
• Logo by itself on one side

```html
<!DOCTYPE html>
<html lang="en">
<head>
<meta charset="utf-8">
<title>Corvale Spine &amp; Joint – Business Card</title>
<link rel="stylesheet" href="https://fonts.googleapis.com/css2?family=Barlow:wght@400;500;600;700&display=swap">
<style>
  :root {
    --page: #ffffff;
    --card-white: #ffffff;
    --brand-grey: #a3b4bb;
    --brand-blue: #6580b0;
    --text-grey: #9fb0b7;
    --logo-white: #ffffff;
    --shadow: rgba(0, 0, 0, 0.18);
  }
  * { margin: 0; padding: 0; box-sizing: border-box; }
  html, body {
    width: 1200px; height: 1200px; overflow: hidden;
    background: var(--page);
    font-family: "Barlow", Arial, sans-serif;
  }
  .sheet { position: relative; width: 1200px; height: 1200px; }
  .card {
    position: absolute; left: 160px; width: 880px; height: 500px;
    overflow: hidden;
    box-shadow: 0 8px 28px var(--shadow);
  }
  .card--front { top: 60px; background: var(--card-white); }
  .card--back { top: 640px; background: var(--brand-grey); }

  .front-wave { position: absolute; inset: 0; width: 880px; height: 500px; }

  .identity { position: absolute; left: 70px; top: 100px; }
  .identity__name {
    font-weight: 700; font-size: 60px; line-height: 1; color: var(--brand-blue);
  }
  .identity__title {
    font-weight: 500; font-size: 58px; line-height: 1; color: var(--text-grey);
    margin-top: 18px;
  }
  .identity__phone {
    display: flex; align-items: center; gap: 16px;
    margin-top: 20px; margin-left: 20px;
    font-size: 25px; color: var(--brand-blue);
  }

  .locations { position: absolute; left: 590px; top: 34px; }
  .location { margin-bottom: 10px; }
  .location__city {
    font-weight: 600; font-size: 22px; color: var(--text-grey); letter-spacing: 0.3px;
    line-height: 1.15;
  }
  .location__line {
    display: flex; align-items: center; gap: 10px;
    font-size: 20px; color: var(--brand-blue); line-height: 1.2;
  }
  .icon { width: 20px; height: 20px; flex: none; }
  .identity__phone .icon { width: 24px; height: 24px; }

  .brand-name { color: var(--logo-white); font-weight: 500; text-align: center; }
  .brand-name--front { position: absolute; right: 40px; top: 398px; }
  .brand-name--front .brand-name__main { font-size: 38px; letter-spacing: 6px; line-height: 1; }
  .brand-name--front .brand-name__sub { font-size: 17px; letter-spacing: 4px; margin-top: 6px; }

  .brand-name--back {
    position: absolute; left: 0; right: 0; top: 50%; transform: translateY(-50%);
  }
  .brand-name--back .brand-name__main { font-size: 104px; letter-spacing: 16px; line-height: 1; }
  .brand-name--back .brand-name__sub { font-size: 40px; letter-spacing: 12px; margin-top: 14px; }
</style>
</head>
<body>
<main class="sheet">

  <section class="card card--front" aria-label="Business card front">
    <svg class="front-wave" viewBox="0 0 880 500" aria-hidden="true">
      <path d="M0,318 C200,380 420,400 600,352 C720,320 800,306 880,304 L880,500 L0,500 Z" fill="var(--brand-blue)"/>
      <path d="M0,344 C200,408 420,424 606,374 C726,342 806,332 880,330 L880,500 L0,500 Z" fill="var(--card-white)"/>
      <path d="M0,358 C200,424 430,440 616,388 C736,356 814,346 880,344 L880,500 L0,500 Z" fill="var(--brand-grey)"/>
    </svg>

    <div class="identity">
      <h1 class="identity__name">YOUR NAME</h1>
      <p class="identity__title">CEO</p>
      <p class="identity__phone">
        <svg class="icon" viewBox="0 0 24 24" aria-hidden="true"><path fill="var(--brand-blue)" d="M6.6 10.8c1.4 2.8 3.8 5.1 6.6 6.6l2.2-2.2c.3-.3.7-.4 1-.2 1.1.4 2.3.6 3.6.6.6 0 1 .4 1 1V20c0 .6-.4 1-1 1C10.6 21 3 13.4 3 4c0-.6.4-1 1-1h3.5c.6 0 1 .4 1 1 0 1.3.2 2.5.6 3.6.1.3 0 .7-.2 1z"/></svg>
        555-555-555
      </p>
    </div>

    <div class="locations">
      <div class="location">
        <h2 class="location__city">BROOKMERE</h2>
        <p class="location__line"><svg class="icon" viewBox="0 0 24 24" aria-hidden="true"><path fill="var(--brand-blue)" d="M6.6 10.8c1.4 2.8 3.8 5.1 6.6 6.6l2.2-2.2c.3-.3.7-.4 1-.2 1.1.4 2.3.6 3.6.6.6 0 1 .4 1 1V20c0 .6-.4 1-1 1C10.6 21 3 13.4 3 4c0-.6.4-1 1-1h3.5c.6 0 1 .4 1 1 0 1.3.2 2.5.6 3.6.1.3 0 .7-.2 1z"/></svg>333-333-333</p>
        <p class="location__line"><svg class="icon" viewBox="0 0 24 24" aria-hidden="true"><path fill="none" stroke="var(--brand-blue)" stroke-width="1.6" d="M12 22s7-7.2 7-12.5A7 7 0 0 0 5 9.5C5 14.8 12 22 12 22z"/><circle cx="12" cy="9.5" r="2.6" fill="none" stroke="var(--brand-blue)" stroke-width="1.6"/></svg>Stret-number</p>
      </div>
      <div class="location">
        <h2 class="location__city">WESTHAVEN</h2>
        <p class="location__line"><svg class="icon" viewBox="0 0 24 24" aria-hidden="true"><path fill="var(--brand-blue)" d="M6.6 10.8c1.4 2.8 3.8 5.1 6.6 6.6l2.2-2.2c.3-.3.7-.4 1-.2 1.1.4 2.3.6 3.6.6.6 0 1 .4 1 1V20c0 .6-.4 1-1 1C10.6 21 3 13.4 3 4c0-.6.4-1 1-1h3.5c.6 0 1 .4 1 1 0 1.3.2 2.5.6 3.6.1.3 0 .7-.2 1z"/></svg>222-222-222</p>
        <p class="location__line"><svg class="icon" viewBox="0 0 24 24" aria-hidden="true"><path fill="none" stroke="var(--brand-blue)" stroke-width="1.6" d="M12 22s7-7.2 7-12.5A7 7 0 0 0 5 9.5C5 14.8 12 22 12 22z"/><circle cx="12" cy="9.5" r="2.6" fill="none" stroke="var(--brand-blue)" stroke-width="1.6"/></svg>Stret-number</p>
      </div>
      <div class="location">
        <h2 class="location__city">LARKFIELD</h2>
        <p class="location__line"><svg class="icon" viewBox="0 0 24 24" aria-hidden="true"><path fill="var(--brand-blue)" d="M6.6 10.8c1.4 2.8 3.8 5.1 6.6 6.6l2.2-2.2c.3-.3.7-.4 1-.2 1.1.4 2.3.6 3.6.6.6 0 1 .4 1 1V20c0 .6-.4 1-1 1C10.6 21 3 13.4 3 4c0-.6.4-1 1-1h3.5c.6 0 1 .4 1 1 0 1.3.2 2.5.6 3.6.1.3 0 .7-.2 1z"/></svg>444-444-444</p>
        <p class="location__line"><svg class="icon" viewBox="0 0 24 24" aria-hidden="true"><path fill="none" stroke="var(--brand-blue)" stroke-width="1.6" d="M12 22s7-7.2 7-12.5A7 7 0 0 0 5 9.5C5 14.8 12 22 12 22z"/><circle cx="12" cy="9.5" r="2.6" fill="none" stroke="var(--brand-blue)" stroke-width="1.6"/></svg>Stret-number</p>
      </div>
    </div>

    <div class="brand-name brand-name--front">
      <p class="brand-name__main">CORVALE</p>
      <p class="brand-name__sub">SPINE &amp; JOINT</p>
    </div>
  </section>

  <section class="card card--back" aria-label="Business card back">
    <div class="brand-name brand-name--back">
      <p class="brand-name__main">CORVALE</p>
      <p class="brand-name__sub">SPINE &amp; JOINT</p>
    </div>
  </section>

</main>
</body>
</html>
```